Velmora Strom GmbH webpage The online Business card of a master electrician

A clean, modern webpage on whitch i can show my clients what im capable of and where the future costumer can inform himself. I need a login page for costumers who are registred and an secound webpage where my stuff can login to report theyr labour.
I will post pictures before and after, put on some commercial and crossellimg informations.
The costumer should find my insta as well my twitter or snapchat accounts.

Update:
Our Services are, Installations, Renovations, Home Automation, CCTV, Telefon / VOIP, Networking / Network-Cabeling, Electrical Supervisioning

Target Market(s)

Private and business costumers

Industry/Entity Type

Electric Company

Number of Pages Required

5+ page

Font styles to use
Sans Serif
Other font styles liked:
• Zurich,

Colors

Designer to choose colors to be used in the design.

Requirements
Must have
• A Page Hero
• A Costumer and staff login page (2separate pages)
• Contact form
• Responsive form
• Photo Feed enbedding account velmora_strom
Nice to have
• A Blog

```html
<!DOCTYPE html>
<html lang="en">
<head>
<meta charset="utf-8">
<title>Blog – Velmora Strom</title>
<link rel="stylesheet" href="https://fonts.googleapis.com/css2?family=Open+Sans:wght@400;600;700&display=swap">
<style>
:root{
  --blue:#0b4c9c;
  --blue-light:#2f8fe0;
  --dark:#2b2b2b;
  --footer:#2a2a2a;
  --footer-bottom:#222;
  --text:#555;
  --heading:#222;
  --line:#dcdcdc;
  --muted:#888;
  --white:#fff;
}
*{box-sizing:border-box;margin:0;padding:0}
html,body{width:1200px;height:2384px;overflow:hidden}
body{position:relative;font-family:"Open Sans",Arial,sans-serif;color:var(--text);background:var(--white)}
a{color:inherit;text-decoration:none}
svg{display:block}

/* top bar */
.topbar{position:absolute;left:0;top:0;width:1200px;height:35px;background:var(--dark);color:#eee;font-size:13px}
.topbar .socials{position:absolute;left:38px;top:0;display:flex;height:35px}
.topbar .socials span{width:35px;height:35px;border-right:1px solid #444;display:flex;align-items:center;justify-content:center}
.topbar .socials span:first-child{border-left:1px solid #444}
.topbar .socials i{width:11px;height:11px;background:#ddd;display:block}
.topbar .contact{position:absolute;right:38px;top:0;height:35px;display:flex;align-items:center;gap:22px}
.topbar .contact span{display:flex;align-items:center;gap:7px}

/* header */
.header{position:absolute;left:0;top:35px;width:1200px;height:76px;background:var(--white);box-shadow:0 1px 3px rgba(0,0,0,.08)}
.brand{position:absolute;left:38px;top:22px;display:flex;align-items:center;gap:10px;font-size:26px;font-weight:700;color:var(--blue)}
.brand i{width:26px;height:26px;background:var(--blue);display:block}
.nav{position:absolute;top:0;left:0;height:76px;width:100%}
.nav a{position:absolute;top:31px;font-size:14px;color:#777;letter-spacing:.3px}
.nav a.active{color:var(--blue)}
.nav a.active::after{content:"";position:absolute;left:0;right:0;top:42px;height:3px;background:var(--blue)}

/* hero */
.hero{position:absolute;left:0;top:111px;width:1200px;height:259px;background:linear-gradient(100deg,#3a3a36 0%,#5a5f52 35%,#4b5248 60%,#2e3130 100%)}
.hero::after{content:"";position:absolute;inset:0;background:rgba(0,0,0,.35)}
.hero-text{position:absolute;left:0;right:0;top:108px;text-align:center;color:var(--white);z-index:1}
.hero-text h1{font-size:32px;font-weight:700;letter-spacing:1px}
.hero-text p{font-size:13px;margin-top:6px}
.hero-text p b{color:var(--blue-light);font-weight:400}

/* blog cards */
.card{position:absolute;width:393px;height:505px;border:1px solid var(--line);background:var(--white)}
.card-media{position:relative;height:264px}
.card-title{position:absolute;left:0;right:0;bottom:0;height:41px;background:rgba(0,0,0,.6);color:var(--white);font-size:14px;font-weight:700;padding:0 16px;line-height:41px;text-transform:uppercase}
.slide-arrow{position:absolute;top:108px;width:44px;height:44px;background:rgba(0,0,0,.75);display:flex;align-items:center;justify-content:center}
.play{position:absolute;left:50%;top:50%;transform:translate(-50%,-60%);width:44px;height:44px;border:2px solid #fff;border-radius:50%;display:flex;align-items:center;justify-content:center}
.card-body{text-align:center;padding:22px 20px 0;height:200px}
.author{font-size:13px;color:#666}
.author b{color:#222;font-weight:700}
.excerpt{font-size:13.5px;line-height:21px;color:#777;margin-top:12px}
.read-more{display:inline-flex;align-items:center;gap:10px;margin-top:11px;font-size:14px;font-weight:600;color:var(--blue)}
.card-meta{position:absolute;left:0;right:0;bottom:0;height:40px;border-top:1px solid var(--line);display:flex}
.card-meta span{flex:1;display:flex;align-items:center;justify-content:center;gap:6px;font-size:12px;color:#444;border-left:1px solid var(--line)}
.card-meta span:first-child{border-left:0}
.card-meta span.liked{background:var(--blue);color:var(--white)}

/* sidebar */
.sidebar{position:absolute;left:883px;top:435px;width:279px}
.search{height:42px;border:1px solid var(--line);display:flex;align-items:center;justify-content:space-between;padding:0 12px;font-size:13px;color:#777}
.widget-title{font-size:17px;font-weight:700;color:var(--heading);display:flex;align-items:center;gap:8px}
.widget-title::after{content:"";width:34px;height:3px;background:var(--blue);margin-top:6px}
.categories{margin-top:12px;list-style:none}
.categories li{height:34px;border-bottom:1px solid #e4e4e4;display:flex;align-items:center;gap:8px;font-size:12.5px;color:#666}
.recent{list-style:none;margin-top:18px}
.recent li{display:flex;gap:14px;height:110px}
.thumb{width:98px;height:86px;border:1px solid var(--line);padding:3px;flex:none}
.thumb div{width:100%;height:100%}
.recent h4{font-size:14px;font-weight:700;color:#222;margin-top:0}
.recent p{font-size:12px;line-height:17px;color:#777;margin-top:3px}

/* pagination */
.pagination{position:absolute;left:284px;top:1511px;display:flex;gap:9px}
.pagination span{width:38px;height:38px;border:1px solid #ccc;border-radius:50%;display:flex;align-items:center;justify-content:center;font-size:14px;color:#777}
.pagination span.current{border-color:var(--blue);color:var(--blue);border-width:1.5px}

/* photo feed */
.feed-title{position:absolute;left:0;right:0;top:1630px;display:flex;justify-content:center;align-items:center;gap:10px;font-size:26px;font-weight:600;color:#222}
.feed-title i{width:32px;height:32px;border:2px solid #b03a7a;border-radius:8px;display:block}
.feed-grid{position:absolute;left:296px;top:1689px;width:608px;display:grid;grid-template-columns:repeat(4,140px);gap:16px 16px}
.feed-grid div{height:124px}
.feed-button{position:absolute;left:517px;top:1966px;width:166px;height:35px;background:var(--blue);color:var(--white);border-radius:3px;display:flex;align-items:center;justify-content:center;gap:8px;font-size:13px;font-weight:600}
.feed-button i{width:14px;height:14px;border:1.5px solid #fff;border-radius:3px;display:block}

/* footer */
.footer{position:absolute;left:0;top:2082px;width:1200px;height:254px;background:var(--footer);border-top:4px solid var(--blue);color:#ccc}
.footer h3{position:absolute;top:30px;font-size:15px;font-weight:700;color:var(--white);letter-spacing:.5px}
.footer h3::after{content:"";display:block;width:40px;height:2px;background:var(--blue);margin-top:6px}
.f-contact{position:absolute;left:38px;top:82px;list-style:none;font-size:13px}
.f-contact li{display:flex;gap:14px;align-items:flex-start;margin-bottom:17px;line-height:17px}
.f-menu{position:absolute;top:90px;list-style:none;font-size:12.5px;text-transform:uppercase}
.f-menu li{height:33px;display:flex;gap:10px;align-items:flex-start}
.f-about{position:absolute;left:858px;top:86px;width:304px;text-align:center;font-size:13px;line-height:21px}
.f-social{display:flex;justify-content:center;gap:18px;margin-top:26px}
.f-social i{width:12px;height:12px;background:#eee;display:block}
.copyright{position:absolute;left:0;top:2336px;width:1200px;height:48px;background:var(--footer-bottom);border-top:1px solid #3a3a3a;color:#ccc;font-size:11px;display:flex;align-items:center;justify-content:center}
.copyright b{color:var(--blue-light);font-weight:400;margin:0 3px}
</style>
</head>
<body>

<div class="topbar">
  <div class="socials"><span><i></i></span><span><i></i></span><span><i></i></span><span><i></i></span><span><i></i></span></div>
  <div class="contact">
    <span><svg width="12" height="12" viewBox="0 0 24 24"><path fill="#eee" d="M6.6 10.8a15 15 0 006.6 6.6l2.2-2.2c.3-.3.7-.4 1-.2 1.1.4 2.3.6 3.6.6.6 0 1 .4 1 1V20c0 .6-.4 1-1 1A17 17 0 013 4c0-.6.4-1 1-1h3.5c.6 0 1 .4 1 1 0 1.3.2 2.5.6 3.6.1.3 0 .7-.2 1z"/></svg>123 456 7890</span>
    <span><svg width="14" height="12" viewBox="0 0 24 20"><rect x="1" y="1" width="22" height="18" rx="2" fill="none" stroke="#eee" stroke-width="2"/><path d="M1 2l11 9 11-9" fill="none" stroke="#eee" stroke-width="2"/></svg>info@velmorastrom.com</span>
  </div>
</div>

<header class="header">
  <div class="brand"><i></i>Velmora Strom</div>
  <nav class="nav">
    <a style="left:577px">HOME</a>
    <a style="left:666px">ABOUT US</a>
    <a style="left:782px">GALLERY</a>
    <a style="left:888px">SERVICE</a>
    <a class="active" style="left:988px">BLOG</a>
    <a style="left:1073px">CONTACT US</a>
  </nav>
</header>

<section class="hero" role="img" aria-label="Close-up of hands soldering a circuit board">
  <div class="hero-text"><h1>BLOG</h1><p>Home &nbsp;» <b>Blog</b></p></div>
</section>

<!-- posts -->
<article class="card" style="left:38px;top:435px">
  <div class="card-media" role="img" aria-label="Suspension bridge lit at sunset" style="background:linear-gradient(180deg,#c9a88e 0%,#b46a3e 45%,#3b2a2a 100%)">
    <div class="slide-arrow" style="left:0"><svg width="12" height="18" viewBox="0 0 12 18"><path d="M10 2L3 9l7 7" fill="none" stroke="#fff" stroke-width="2.5"/></svg></div>
    <div class="slide-arrow" style="right:0"><svg width="12" height="18" viewBox="0 0 12 18"><path d="M2 2l7 7-7 7" fill="none" stroke="#fff" stroke-width="2.5"/></svg></div>
    <div class="card-title">Lorem ipsum dolor sit amet...</div>
  </div>
  <div class="card-body">
    <p class="author">Posted by <b>Lukas Brandt</b></p>
    <p class="excerpt">Lorem ipsum dolor sit amet, consectetur adipiscing elit, sed do eiusmod tempor incididunt ut labore et dolore magna aliqua. Ut enim ad minim veniam, quis nostrud exercitation ullamco laboris nisi ut aliquip commodo consequat.[...]</p>
    <a class="read-more">Read More <svg width="16" height="8" viewBox="0 0 16 8"><path d="M0 4h13M10 1l3 3-3 3" fill="none" stroke="#0b4c9c" stroke-width="2"/></svg></a>
  </div>
  <div class="card-meta">
    <span><svg width="11" height="11" viewBox="0 0 12 12"><rect x="1" y="2" width="10" height="9" fill="none" stroke="#444" stroke-width="1.4"/><path d="M1 5h10M4 0v3M8 0v3" stroke="#444" stroke-width="1.4"/></svg>22 Jun 2016</span>
    <span><svg width="12" height="11" viewBox="0 0 12 11"><path d="M6 1C3 1 1 2.7 1 5c0 1.2.6 2.2 1.5 2.9L2 10l2.6-1.3c.4.1.9.2 1.4.2 3 0 5-1.7 5-4S9 1 6 1z" fill="none" stroke="#444" stroke-width="1.2"/></svg>3 Comment</span>
    <span class="liked"><svg width="12" height="11" viewBox="0 0 12 11"><path d="M6 10L1.5 5.5A2.6 2.6 0 016 2a2.6 2.6 0 014.5 3.5z" fill="none" stroke="#fff" stroke-width="1.3"/></svg>10 Likes</span>
  </div>
</article>

<article class="card" style="left:461px;top:435px">
  <div class="card-media" role="img" aria-label="Reception lobby with blue LED ceiling lighting" style="background:linear-gradient(180deg,#6a4fd0 0%,#5b3a4a 40%,#7a4a28 70%,#2c2420 100%)">
    <div class="card-title">Lorem ipsum dolor sit...</div>
  </div>
  <div class="card-body">
    <p class="author">Posted by <b>Tomas Verel</b></p>
    <p class="excerpt">Lorem ipsum dolor sit amet, consectetur adipiscing elit, sed do eiusmod tempor incididunt ut labore et dolore magna aliqua. Ut enim ad minim veniam, quis nostrud exercitation ullamco laboris nisi ut aliquip commodo consequat.[...]</p>
    <a class="read-more">Read More <svg width="16" height="8" viewBox="0 0 16 8"><path d="M0 4h13M10 1l3 3-3 3" fill="none" stroke="#0b4c9c" stroke-width="2"/></svg></a>
  </div>
  <div class="card-meta">
    <span><svg width="11" height="11" viewBox="0 0 12 12"><rect x="1" y="2" width="10" height="9" fill="none" stroke="#444" stroke-width="1.4"/><path d="M1 5h10M4 0v3M8 0v3" stroke="#444" stroke-width="1.4"/></svg>30 Aug 2016</span>
    <span><svg width="12" height="11" viewBox="0 0 12 11"><path d="M6 1C3 1 1 2.7 1 5c0 1.2.6 2.2 1.5 2.9L2 10l2.6-1.3c.4.1.9.2 1.4.2 3 0 5-1.7 5-4S9 1 6 1z" fill="none" stroke="#444" stroke-width="1.2"/></svg>3 Comment</span>
    <span><svg width="12" height="11" viewBox="0 0 12 11"><path d="M6 10L1.5 5.5A2.6 2.6 0 016 2a2.6 2.6 0 014.5 3.5z" fill="none" stroke="#444" stroke-width="1.3"/></svg>25 Likes</span>
  </div>
</article>

<article class="card" style="left:38px;top:971px">
  <div class="card-media" role="img" aria-label="Tool belt and hard hat in front of a house under construction" style="background:linear-gradient(135deg,#8cc0e8 0%,#c9c2b8 45%,#9a7a66 75%,#4a3a30 100%)">
    <div class="card-title">Lorem ipsum dolor sit amet...</div>
  </div>
  <div class="card-body">
    <p class="author">Posted by <b>Admin</b></p>
    <p class="excerpt">Lorem ipsum dolor sit amet, consectetur adipiscing elit, sed do eiusmod tempor incididunt ut labore et dolore magna aliqua. Ut enim ad minim veniam, quis nostrud exercitation ullamco laboris nisi ut aliquip commodo consequat.[...]</p>
    <a class="read-more">Read More <svg width="16" height="8" viewBox="0 0 16 8"><path d="M0 4h13M10 1l3 3-3 3" fill="none" stroke="#0b4c9c" stroke-width="2"/></svg></a>
  </div>
  <div class="card-meta">
    <span><svg width="11" height="11" viewBox="0 0 12 12"><rect x="1" y="2" width="10" height="9" fill="none" stroke="#444" stroke-width="1.4"/><path d="M1 5h10M4 0v3M8 0v3" stroke="#444" stroke-width="1.4"/></svg>10 Feb 2015</span>
    <span><svg width="12" height="11" viewBox="0 0 12 11"><path d="M6 1C3 1 1 2.7 1 5c0 1.2.6 2.2 1.5 2.9L2 10l2.6-1.3c.4.1.9.2 1.4.2 3 0 5-1.7 5-4S9 1 6 1z" fill="none" stroke="#444" stroke-width="1.2"/></svg>5 Comment</span>
    <span><svg width="12" height="11" viewBox="0 0 12 11"><path d="M6 10L1.5 5.5A2.6 2.6 0 016 2a2.6 2.6 0 014.5 3.5z" fill="none" stroke="#444" stroke-width="1.3"/></svg>10 Likes</span>
  </div>
</article>

<article class="card" style="left:461px;top:971px">
  <div class="card-media" role="img" aria-label="Engineer reviewing a floor plan at a desk" style="background:linear-gradient(135deg,#9fb0b4 0%,#c8cfd2 40%,#3d5a8a 70%,#2a2a2e 100%)">
    <div class="play"><svg width="14" height="16" viewBox="0 0 14 16"><path d="M2 1l11 7-11 7z" fill="#fff"/></svg></div>
    <div class="card-title">Lorem ipsum dolor sit...</div>
  </div>
  <div class="card-body">
    <p class="author">Posted by <b>Admin</b></p>
    <p class="excerpt">Lorem ipsum dolor sit amet, consectetur adipiscing elit, sed do eiusmod tempor incididunt ut labore et dolore magna aliqua. Ut enim ad minim veniam, quis nostrud exercitation ullamco laboris nisi ut aliquip commodo consequat.[...]</p>
    <a class="read-more">Read More <svg width="16" height="8" viewBox="0 0 16 8"><path d="M0 4h13M10 1l3 3-3 3" fill="none" stroke="#0b4c9c" stroke-width="2"/></svg></a>
  </div>
  <div class="card-meta">
    <span><svg width="11" height="11" viewBox="0 0 12 12"><rect x="1" y="2" width="10" height="9" fill="none" stroke="#444" stroke-width="1.4"/><path d="M1 5h10M4 0v3M8 0v3" stroke="#444" stroke-width="1.4"/></svg>30 Aug 2016</span>
    <span><svg width="12" height="11" viewBox="0 0 12 11"><path d="M6 1C3 1 1 2.7 1 5c0 1.2.6 2.2 1.5 2.9L2 10l2.6-1.3c.4.1.9.2 1.4.2 3 0 5-1.7 5-4S9 1 6 1z" fill="none" stroke="#444" stroke-width="1.2"/></svg>3 Comment</span>
    <span><svg width="12" height="11" viewBox="0 0 12 11"><path d="M6 10L1.5 5.5A2.6 2.6 0 016 2a2.6 2.6 0 014.5 3.5z" fill="none" stroke="#444" stroke-width="1.3"/></svg>25 Likes</span>
  </div>
</article>

<aside class="sidebar">
  <div class="search">Search...<svg width="14" height="14" viewBox="0 0 14 14"><circle cx="6" cy="6" r="4.5" fill="none" stroke="#222" stroke-width="2"/><path d="M9.5 9.5L13 13" stroke="#222" stroke-width="2"/></svg></div>
  <h3 class="widget-title" style="margin-top:28px">Categories</h3>
  <ul class="categories">
    <li><svg width="12" height="7" viewBox="0 0 12 7"><path d="M0 3.5h10M8 1l2.5 2.5L8 6" fill="none" stroke="#555" stroke-width="1.2"/></svg>Lorem ipsum dolor</li>
    <li><svg width="12" height="7" viewBox="0 0 12 7"><path d="M0 3.5h10M8 1l2.5 2.5L8 6" fill="none" stroke="#555" stroke-width="1.2"/></svg>Lorem ipsum dolor</li>
    <li><svg width="12" height="7" viewBox="0 0 12 7"><path d="M0 3.5h10M8 1l2.5 2.5L8 6" fill="none" stroke="#555" stroke-width="1.2"/></svg>Lorem ipsum dolor</li>
    <li><svg width="12" height="7" viewBox="0 0 12 7"><path d="M0 3.5h10M8 1l2.5 2.5L8 6" fill="none" stroke="#555" stroke-width="1.2"/></svg>Lorem ipsum dolor</li>
    <li><svg width="12" height="7" viewBox="0 0 12 7"><path d="M0 3.5h10M8 1l2.5 2.5L8 6" fill="none" stroke="#555" stroke-width="1.2"/></svg>Lorem ipsum dolor</li>
    <li><svg width="12" height="7" viewBox="0 0 12 7"><path d="M0 3.5h10M8 1l2.5 2.5L8 6" fill="none" stroke="#555" stroke-width="1.2"/></svg>Lorem ipsum dolor</li>
    <li><svg width="12" height="7" viewBox="0 0 12 7"><path d="M0 3.5h10M8 1l2.5 2.5L8 6" fill="none" stroke="#555" stroke-width="1.2"/></svg>Lorem ipsum dolor</li>
    <li><svg width="12" height="7" viewBox="0 0 12 7"><path d="M0 3.5h10M8 1l2.5 2.5L8 6" fill="none" stroke="#555" stroke-width="1.2"/></svg>Lorem ipsum dolor</li>
    <li style="border-bottom:0"><svg width="12" height="7" viewBox="0 0 12 7"><path d="M0 3.5h10M8 1l2.5 2.5L8 6" fill="none" stroke="#555" stroke-width="1.2"/></svg>Lorem ipsum dolor</li>
  </ul>
  <h3 class="widget-title" style="margin-top:40px">Recent Posts</h3>
  <ul class="recent">
    <li><div class="thumb"><div role="img" aria-label="Two electricians with toolboxes" style="background:linear-gradient(135deg,#a8b8c8,#3a4a6a)"></div></div><div><h4>Lorem Ipsum is simply.</h4><p>Lorem Ipsum is simply dummy text of the printing and typesetting industry.</p></div></li>
    <li><div class="thumb"><div role="img" aria-label="Worker on a brick wall" style="background:linear-gradient(135deg,#c9ccd0,#7a4a3a)"></div></div><div><h4>Lorem Ipsum is simply.</h4><p>Lorem Ipsum is simply dummy text of the printing and typesetting industry.</p></div></li>
    <li><div class="thumb"><div role="img" aria-label="Workers in high-visibility vests" style="background:linear-gradient(135deg,#d8a060,#e06a20)"></div></div><div><h4>Lorem Ipsum is simply.</h4><p>Lorem Ipsum is simply dummy text of the printing and typesetting industry.</p></div></li>
    <li><div class="thumb"><div role="img" aria-label="Electrician at a switchboard" style="background:linear-gradient(135deg,#c0c8d4,#2a5a9a)"></div></div><div><h4>Lorem Ipsum is simply.</h4><p>Lorem Ipsum is simply dummy text of the printing and typesetting industry.</p></div></li>
    <li><div class="thumb"><div role="img" aria-label="Technician servicing equipment" style="background:linear-gradient(135deg,#8a9ab0,#1e3a6a)"></div></div><div><h4>Lorem Ipsum is simply.</h4><p>Lorem Ipsum is simply dummy text of the printing and typesetting industry.</p></div></li>
  </ul>
</aside>

<nav class="pagination">
  <span><svg width="14" height="8" viewBox="0 0 14 8"><path d="M14 4H2M5 1L2 4l3 3" fill="none" stroke="#555" stroke-width="1.4"/></svg></span>
  <span class="current">1</span><span>2</span><span>3</span><span>···</span>
  <span><svg width="14" height="8" viewBox="0 0 14 8"><path d="M0 4h12M9 1l3 3-3 3" fill="none" stroke="#555" stroke-width="1.4"/></svg></span>
</nav>

<h2 class="feed-title"><i></i>Photo Feed</h2>
<div class="feed-grid">
  <div role="img" aria-label="Control cabinet wiring" style="background:linear-gradient(135deg,#6a6a5a,#2e3a34)"></div>
  <div role="img" aria-label="Circuit boards on a workbench" style="background:linear-gradient(135deg,#d8ccb8,#7a6a5a)"></div>
  <div role="img" aria-label="Cup of coffee on a saucer" style="background:linear-gradient(135deg,#3a3a3a,#e8e4de)"></div>
  <div role="img" aria-label="Control cabinet wiring" style="background:linear-gradient(135deg,#6a6a5a,#2e3a34)"></div>
  <div role="img" aria-label="Cup of coffee on a saucer" style="background:linear-gradient(135deg,#3a3a3a,#e8e4de)"></div>
  <div role="img" aria-label="Control cabinet wiring" style="background:linear-gradient(135deg,#6a6a5a,#2e3a34)"></div>
  <div role="img" aria-label="Circuit boards on a workbench" style="background:linear-gradient(135deg,#d8ccb8,#7a6a5a)"></div>
  <div role="img" aria-label="Cup of coffee on a saucer" style="background:linear-gradient(135deg,#3a3a3a,#e8e4de)"></div>
</div>
<a class="feed-button"><i></i>View Photo Feed</a>

<footer class="footer">
  <h3 style="left:38px">CONTACT</h3>
  <ul class="f-contact">
    <li><svg width="12" height="16" viewBox="0 0 12 16"><path d="M6 0a6 6 0 00-6 6c0 4.5 6 10 6 10s6-5.5 6-10a6 6 0 00-6-6zm0 8.5A2.5 2.5 0 116 3.5a2.5 2.5 0 010 5z" fill="#eee"/></svg>2417 Corran St Dalemont,<br>CA 93104.</li>
    <li><svg width="13" height="13" viewBox="0 0 24 24"><path fill="#eee" d="M6.6 10.8a15 15 0 006.6 6.6l2.2-2.2c.3-.3.7-.4 1-.2 1.1.4 2.3.6 3.6.6.6 0 1 .4 1 1V20c0 .6-.4 1-1 1A17 17 0 013 4c0-.6.4-1 1-1h3.5c.6 0 1 .4 1 1 0 1.3.2 2.5.6 3.6.1.3 0 .7-.2 1z"/></svg>123 456 7890</li>
    <li><svg width="14" height="12" viewBox="0 0 24 20"><rect x="1" y="1" width="22" height="18" rx="2" fill="none" stroke="#eee" stroke-width="2"/><path d="M1 2l11 9 11-9" fill="none" stroke="#eee" stroke-width="2"/></svg>info@velmorastrom.com</li>
    <li><svg width="14" height="14" viewBox="0 0 14 14"><circle cx="7" cy="7" r="6" fill="#eee"/><path d="M1 7h12M7 1c-2 2-2 10 0 12M7 1c2 2 2 10 0 12" fill="none" stroke="#2a2a2a" stroke-width="1"/></svg>www.velmorastrom.com</li>
  </ul>

  <h3 style="left:399px">MENU LINK</h3>
  <ul class="f-menu" style="left:399px">
    <li><svg width="12" height="8" viewBox="0 0 12 8"><path d="M0 4h10M7 1l3 3-3 3" fill="none" stroke="#2f8fe0" stroke-width="1.5"/></svg>Home</li>
    <li><svg width="12" height="8" viewBox="0 0 12 8"><path d="M0 4h10M7 1l3 3-3 3" fill="none" stroke="#2f8fe0" stroke-width="1.5"/></svg>Gallery</li>
    <li><svg width="12" height="8" viewBox="0 0 12 8"><path d="M0 4h10M7 1l3 3-3 3" fill="none" stroke="#2f8fe0" stroke-width="1.5"/></svg>Blog</li>
    <li><svg width="12" height="8" viewBox="0 0 12 8"><path d="M0 4h10M7 1l3 3-3 3" fill="none" stroke="#2f8fe0" stroke-width="1.5"/></svg>Privacy Policy</li>
  </ul>
  <ul class="f-menu" style="left:607px">
    <li><svg width="12" height="8" viewBox="0 0 12 8"><path d="M0 4h10M7 1l3 3-3 3" fill="none" stroke="#2f8fe0" stroke-width="1.5"/></svg>About Us</li>
    <li><svg width="12" height="8" viewBox="0 0 12 8"><path d="M0 4h10M7 1l3 3-3 3" fill="none" stroke="#2f8fe0" stroke-width="1.5"/></svg>Service</li>
    <li><svg width="12" height="8" viewBox="0 0 12 8"><path d="M0 4h10M7 1l3 3-3 3" fill="none" stroke="#2f8fe0" stroke-width="1.5"/></svg>Contact Us</li>
    <li><svg width="12" height="8" viewBox="0 0 12 8"><path d="M0 4h10M7 1l3 3-3 3" fill="none" stroke="#2f8fe0" stroke-width="1.5"/></svg>Terms &amp; Conditions</li>
  </ul>

  <h3 style="left:858px">ABOUT</h3>
  <div class="f-about">
    <p>Lorem ipsum dolor sit amet, consectetur adi-piscing elit, sed do eiusmod tempor incididunt ut labore et dolore magna aliqua. Ut enim ad minim veniam, quis nostrud consequat.</p>
    <div class="f-social"><i></i><i></i><i></i><i></i><i></i></div>
  </div>
</footer>
<div class="copyright">Copyright © 2017 <b>VelmoraStrom.com</b>. All Rights Reserved</div>

</body>
</html>
```